Professional/modern business card design for construction company

We need a new business card design, double sided keeping it modern, sleek, professional and simple. We are an earthmoving business but do not want any pictures of machinery. I would like one side to have the logo and the other to have all the information, keeping with the colors in our logo. The business card will need to be able to be customised so we can use it for several different managers., we would also like to be able to use the design to apply it to other stationary ie. letterheads, notebooks etc. We do not really have a tag line but we could put on there that we specialise in - Agriculture, Civil Construction and Mining.

Contact Information for Business Card

Brolga Ridge Excavations Pty Ltd
ABN 58 402 937 615
82 Gumleaf Creek Road, Moree NSW 2400

Harold Benton
Managing Director
P 0418 639 204
E haroldbenton@brolgaridgeexc.com.au

Font styles to use
Serif
Sans Serif

Requirements
Nice to have
• I have attached some examples of ideas.
Should not have
• images of machinery

```html
<!DOCTYPE html>
<html lang="en">
<head>
<meta charset="utf-8">
<title>Brolga Ridge Excavations – Business Card</title>
<link href="https://fonts.googleapis.com/css2?family=Montserrat:wght@400;500;700;800&display=swap" rel="stylesheet">
<style>
  :root {
    --backdrop: #d3d3d3;
    --paper: #ffffff;
    --charcoal: #444444;
    --slate: #9a9a9a;
    --orange: #f68a22;
    --ink: #3d3d3d;
  }
  * { margin: 0; padding: 0; box-sizing: border-box; }
  html, body {
    width: 900px; height: 1200px; overflow: hidden;
    background: var(--backdrop);
    font-family: "Montserrat", Arial, sans-serif;
  }
  .card { position: absolute; overflow: hidden; }
  .card .shapes { position: absolute; inset: 0; width: 100%; height: 100%; }

  /* Front */
  .card--front { left: 31px; top: 78px; width: 838px; height: 479px; background: var(--paper); }
  .brand-name {
    position: absolute; left: 62px; top: 58px;
    font-weight: 800; font-size: 23px; line-height: 1.2;
    color: var(--charcoal); text-transform: uppercase; letter-spacing: 0.5px;
  }
  .contact-row { position: absolute; left: 54px; display: flex; align-items: center; }
  .contact-row .icon { width: 36px; height: 36px; flex: none; }
  .contact-row .detail {
    margin-left: 13px; font-size: 11px; line-height: 17px; color: var(--ink); font-weight: 400;
  }
  .row-address { top: 269px; }
  .row-phone { top: 333px; }
  .row-email { top: 397px; }
  .signatory {
    position: absolute; left: 515px; top: 423px;
    display: flex; align-items: baseline; color: var(--paper); white-space: nowrap;
  }
  .signatory .role { font-size: 11px; font-weight: 500; margin-right: 7px; }
  .signatory .person { font-size: 24px; font-weight: 700; }

  /* Back */
  .card--back { left: 33px; top: 640px; width: 834px; height: 478px; background: var(--charcoal); }
  .brand-name--centre {
    position: absolute; left: 0; right: 0; top: 205px;
    text-align: center; color: var(--paper);
    font-weight: 800; font-size: 26px; line-height: 1.25;
    text-transform: uppercase; letter-spacing: 0.5px;
  }
</style>
</head>
<body>

<section class="card card--front">
  <svg class="shapes" viewBox="0 0 1117 638" preserveAspectRatio="none" aria-hidden="true">
    <polygon points="744,0 1117,0 897,274" fill="var(--charcoal)"/>
    <polygon points="744,0 897,274 797,399" fill="var(--slate)"/>
    <polygon points="1117,0 1117,638 607,638" fill="var(--orange)"/>
  </svg>

  <div class="brand-name">Brolga Ridge<br>Excavations Pty Ltd</div>

  <div class="contact-row row-address">
    <svg class="icon" viewBox="0 0 36 36" aria-hidden="true">
      <circle cx="18" cy="18" r="16.5" fill="var(--charcoal)" stroke="var(--orange)" stroke-width="2.5"/>
      <path d="M18 8.5c-3.6 0-6.2 2.7-6.2 6.1 0 4.4 6.2 11.9 6.2 11.9s6.2-7.5 6.2-11.9c0-3.4-2.6-6.1-6.2-6.1z" fill="#fff"/>
      <circle cx="18" cy="14.6" r="2.2" fill="var(--charcoal)"/>
    </svg>
    <p class="detail">ABN 58 402 937 615<br>82 Gumleaf Creek Road, Moree NSW 2400</p>
  </div>

  <div class="contact-row row-phone">
    <svg class="icon" viewBox="0 0 36 36" aria-hidden="true">
      <circle cx="18" cy="18" r="16.5" fill="var(--charcoal)" stroke="var(--orange)" stroke-width="2.5"/>
      <path d="M13 9.5l3 .2 1.3 4.4-2 1.5c.9 2.6 2.6 4.7 5 6l1.7-1.8 4.2 1.6-.1 3.1c-.2 1.1-1.3 1.8-2.5 1.6-6.3-1.2-11-6.5-11.9-12.8-.2-1.3.4-2.6 1.3-3.8z" fill="#fff"/>
    </svg>
    <p class="detail">P 0418 639 204</p>
  </div>

  <div class="contact-row row-email">
    <svg class="icon" viewBox="0 0 36 36" aria-hidden="true">
      <circle cx="18" cy="18" r="16.5" fill="var(--charcoal)" stroke="var(--orange)" stroke-width="2.5"/>
      <circle cx="16" cy="16" r="5.5" fill="none" stroke="#fff" stroke-width="2.4"/>
      <line x1="20" y1="20" x2="25.5" y2="25.5" stroke="#fff" stroke-width="3" stroke-linecap="round"/>
    </svg>
    <p class="detail">E haroldbenton@brolgaridgeexc.com.au</p>
  </div>

  <div class="signatory">
    <span class="role">Managing Director:</span>
    <span class="person">Harold Benton</span>
  </div>
</section>

<section class="card card--back">
  <svg class="shapes" viewBox="0 0 1112 636" preserveAspectRatio="none" aria-hidden="true">
    <polygon points="590,0 1112,0 1112,59 532,59" fill="var(--orange)"/>
    <polygon points="0,576 589,576 532,636 0,636" fill="var(--orange)"/>
  </svg>
  <div class="brand-name--centre">Brolga Ridge<br>Excavations Pty Ltd</div>
</section>

</body>
</html>
```